Lindavo Civic Growth Planning New web site

Design a new web site. I have a budget of $1,500.00.
Attached on PowerPoint is a complete site plan. Home page and linked pages.
10 - 12 pages. All copy and photos will be supplied. (300dpi)
I have shown them the concept which they like.
No data bases required. Home page with animations dissolving.
They former web site has been taken down. They have been in business 30 years in New Jersey
Colors teal blues and greens
There will be a new logo)being designed)
The text in home page copy will give you a detailed story what they are all about.
Updates

files have been approved for Lindavo, Inc.   Teodor is the designer

Industry/Entity Type

Community

```html
<!DOCTYPE html>
<html lang="en">
<head>
<meta charset="utf-8">
<title>Lindavo.inc — Community Development Planning</title>
<link rel="stylesheet" href="https://fonts.googleapis.com/css2?family=Josefin+Slab:wght@400;600&family=Open+Sans:wght@400;600;700&display=swap">
<style>
:root{
  --brand:#1a3fd8;
  --brand-dark:#0b24b8;
  --topbar:#0a2ccc;
  --ink:#1d1d1d;
  --muted:#8a8a8a;
  --text:#4a4a4a;
  --card:#ececec;
  --cta-band:#666666;
  --footer:#474747;
  --footer-text:#d6d6d6;
  --white:#ffffff;
}
*{margin:0;padding:0;box-sizing:border-box}
html,body{width:764px;height:1200px;overflow:hidden;background:var(--white)}
.page{position:relative;width:764px;height:1200px;overflow:hidden;font-family:"Open Sans",Arial,sans-serif;color:var(--text)}
.abs{position:absolute}
.slab{font-family:"Josefin Slab",Georgia,serif}

/* top bar */
.topbar{left:0;top:0;width:764px;height:20px;background:var(--topbar)}
.topbar__phone{left:437px;top:3px;font-size:9px;color:var(--white);display:flex;align-items:center;gap:4px;white-space:nowrap}
.topbar__search{left:520px;top:3px;width:128px;height:14px;border:1px solid #8ea2f0;font-size:8px;color:#dfe5ff;padding:1px 5px;display:flex;justify-content:space-between;align-items:center}

/* header */
.brand{left:132px;top:44px;display:flex;align-items:center;gap:7px;font-family:"Josefin Slab",Georgia,serif;font-size:17px;font-weight:600;color:var(--brand);white-space:nowrap}
.brand__mark{width:12px;height:12px;background:var(--brand)}
.nav{left:287px;top:54px;display:flex;gap:15px;font-size:9px;color:#7a7a7a;white-space:nowrap}
.nav a{text-decoration:none;color:inherit}
.nav a.is-active{color:var(--brand)}

/* hero */
.hero__panel{top:92px;height:351px}
.hero__left{left:0;width:243px;background:linear-gradient(180deg,#1e4fa8 0%,#3f73c2 45%,#6d7a86 80%,#39505e 100%)}
.hero__center{left:243px;width:277px;background:linear-gradient(180deg,#e8dccb 0%,#b9a58e 40%,#7f6b58 100%)}
.hero__right{left:520px;width:244px;background:linear-gradient(180deg,#1e4fa8 0%,#3f73c2 45%,#6d7a86 80%,#39505e 100%)}
.hero__band{left:108px;top:218px;width:548px;height:67px;background:rgba(235,235,240,.72);display:flex;align-items:center;justify-content:center;text-align:center;font-family:"Josefin Slab",Georgia,serif;font-size:18.5px;line-height:22px;color:#2a2a2a;font-weight:600;white-space:nowrap}
.btn{display:flex;align-items:center;justify-content:center;color:var(--white);background:linear-gradient(180deg,#2048e6,var(--brand-dark));font-family:"Josefin Slab",Georgia,serif;font-weight:600;white-space:nowrap}
.hero__btn{left:305px;top:323px;width:156px;height:38px;font-size:18px}
.hero__shadow{left:110px;top:443px}

/* sections */
.section-title{left:0;width:764px;text-align:center;font-family:"Josefin Slab",Georgia,serif;font-size:21px;font-weight:600;color:var(--ink);letter-spacing:.5px}
.section-title span{color:var(--brand)}
.welcome__title{top:478px}
.welcome__copy{left:114px;top:509px;width:540px;text-align:center;font-size:8.7px;line-height:10.6px;color:var(--muted)}

.card{top:575px;width:159px;height:230px;background:var(--card)}
.card__photo{left:0;top:0;width:159px;height:185px;border:2px solid #cfcfcf}
.card__caption{left:8px;top:190px;width:143px;text-align:center;font-size:6.5px;line-height:8px;font-weight:700;color:#5a5a5a}
.card__btn{left:28px;top:213px;width:104px;height:26px;font-size:14px}
.card--road{left:116px}
.card--chart{left:304px}
.card--tower{left:491px}
.photo-road{background:linear-gradient(160deg,#3a3f48 0%,#7a5a3a 55%,#c58a4a 75%,#222 100%)}
.photo-chart{background:linear-gradient(160deg,#e9ecef 0%,#c9d6e6 50%,#6fa2cf 100%)}
.photo-tower{background:linear-gradient(90deg,#3b6fc0 0%,#6b9de0 45%,#b25050 75%,#8aaee6 100%)}

.divider{left:116px;top:824px;width:534px;height:1px;background:#e6e6e6}
.results__title{top:844px}
.results__list{width:250px;list-style:none;font-size:8.2px;line-height:10px;color:#555}
.results__list li{position:relative;padding-left:15px;height:32px}
.results__list li::before{content:"»";position:absolute;left:0;top:-3px;color:var(--brand);font-size:12px}
.results__list--left{left:128px;top:889px}
.results__list--right{left:406px;top:888px}

/* call band */
.callband{left:0;top:1029px;width:764px;height:44px;background:var(--cta-band)}
.callband__text{left:119px;top:1045px;font-size:11.5px;color:var(--white);white-space:nowrap}
.callband__btn{left:507px;top:1039px;width:124px;height:26px;font-family:"Open Sans",Arial,sans-serif;font-weight:400;font-size:12px}

/* footer */
.footer{left:0;top:1073px;width:764px;height:127px;background:var(--footer)}
.footer__brand{left:126px;top:1087px;font-family:"Josefin Slab",Georgia,serif;font-size:20px;font-weight:600;color:var(--white);white-space:nowrap}
.footer__social{left:134px;top:1121px;display:flex;gap:2px}
.footer__social span{width:20px;height:20px;border-radius:50%;background:#b8b8b8}
.footer__copy{left:115px;top:1156px;font-size:7.5px;line-height:9px;color:var(--footer-text);white-space:nowrap}
.footer__copy small{color:#8c8c8c;font-size:7px}
.footer__rule{left:248px;top:1083px;width:1px;height:107px;background:#6a6a6a}
.footer__col{top:1090px;font-family:"Josefin Slab",Georgia,serif;color:var(--footer-text)}
.footer__col h4{font-size:11px;font-weight:400;margin-bottom:9px;color:#e8e8e8;white-space:nowrap}
.footer__col li{list-style:none;font-size:9px;line-height:13.6px;white-space:nowrap}
.footer__col--links{left:297px}
.footer__col--places{left:403px}
.footer__col--member{left:492px;width:156px;text-align:center}
.footer__col--member h4{margin-bottom:7px}
.footer__col--member p{font-size:7.8px;line-height:8.6px}
</style>
</head>
<body>
<div class="page">

  <div class="abs topbar"></div>
  <div class="abs topbar__phone">
    <svg width="9" height="9" viewBox="0 0 24 24"><path fill="#fff" d="M6.6 10.8a15.1 15.1 0 0 0 6.6 6.6l2.2-2.2c.3-.3.7-.4 1-.2 1.1.4 2.3.6 3.6.6.6 0 1 .4 1 1V20c0 .6-.4 1-1 1A17 17 0 0 1 3 4c0-.6.4-1 1-1h3.5c.6 0 1 .4 1 1 0 1.3.2 2.5.6 3.6.1.3 0 .7-.2 1z"/></svg>
    (555) 214-0187
  </div>
  <div class="abs topbar__search">Search
    <svg width="9" height="9" viewBox="0 0 24 24"><circle cx="10" cy="10" r="6" stroke="#fff" stroke-width="3" fill="none"/><path d="M15 15l6 6" stroke="#fff" stroke-width="3"/></svg>
  </div>

  <div class="abs brand"><span class="brand__mark"></span>LINDAVO.INC</div>
  <nav class="abs nav slab">
    <a class="is-active" href="#">Home</a>
    <a href="#">Our Company</a>
    <a href="#">Housing Rehab Application</a>
    <a href="#">Affordable Application</a>
    <a href="#">Contact Us</a>
  </nav>

  <div class="abs hero__panel hero__left" role="img" aria-label="City skyline with high-rise towers over the waterfront"></div>
  <div class="abs hero__panel hero__center" role="img" aria-label="Sepia view looking up at a tall office tower"></div>
  <div class="abs hero__panel hero__right" role="img" aria-label="City skyline with high-rise towers over the waterfront"></div>
  <div class="abs hero__band">WE IMPLEMENT LOCAL PROGRAMS TO BENEFIT PEOPLE<br>SEEKING ACCESS TO AFFORDABLE HOUSING.</div>
  <div class="abs btn hero__btn">See more</div>
  <svg class="abs hero__shadow" width="544" height="24" viewBox="0 0 544 24"><defs><radialGradient id="sh" cx="50%" cy="0%" r="60%"><stop offset="0" stop-color="#000" stop-opacity=".28"/><stop offset="1" stop-color="#000" stop-opacity="0"/></radialGradient></defs><ellipse cx="272" cy="0" rx="272" ry="22" fill="url(#sh)"/></svg>

  <h2 class="abs section-title welcome__title">WELCOME TO <span>LINDAVO.INC</span></h2>
  <p class="abs welcome__copy">Lindavo is a city planning firm that specializes in community development and housing rehabilitation program planning, design and implementation. We have over twenty years of experience in developing and administering income base-base housing and programs in accordance with National Office of Housing Renewal (NOHR) and Garden State Housing Access Council (GSHAC) rules and regulations,</p>

  <div class="abs card card--road">
    <div class="abs card__photo photo-road" role="img" aria-label="Highway at dusk with light trails"></div>
    <p class="abs card__caption">Lorem ipsum dolor sit amet, consectetuer adipiscing elit.</p>
    <div class="abs btn card__btn">Learn more</div>
  </div>
  <div class="abs card card--chart">
    <div class="abs card__photo photo-chart" role="img" aria-label="Pen over printed pie chart reports on a desk"></div>
    <p class="abs card__caption">Lorem ipsum dolor sit amet, consectetuer adipiscing elit.</p>
    <div class="abs btn card__btn">Learn more</div>
  </div>
  <div class="abs card card--tower">
    <div class="abs card__photo photo-tower" role="img" aria-label="Office towers against a blue sky"></div>
    <p class="abs card__caption">Lorem ipsum dolor sit amet, consectetuer adipiscing elit.</p>
    <div class="abs btn card__btn">Learn more</div>
  </div>

  <div class="abs divider"></div>
  <h2 class="abs section-title results__title">WE GET <span>RESULT</span></h2>
  <ul class="abs results__list results__list--left">
    <li>Lindavo designs income based programs to be supported by federal placement lotteries state funding.</li>
    <li>We implement local programs to benefit people seeking access to affordable housing.</li>
    <li>Our experienced staff screen applicants for local affordable housing.</li>
  </ul>
  <ul class="abs results__list results__list--right">
    <li>We pre-qualify persons who have applied for housing rehabilitation.</li>
    <li>Our experienced staff screen applicants for local affordable housing.</li>
    <li>Through local housing rehabilitation programs, our experience construction inspectors determine..</li>
  </ul>

  <div class="abs callband"></div>
  <p class="abs callband__text">WANT TO SPEAK TO A LINDAVO.INC? CALL US AT &nbsp;(555) 214-0187</p>
  <div class="abs btn callband__btn">CONTACT US</div>

  <footer class="abs footer"></footer>
  <div class="abs footer__brand">Lindavo.inc</div>
  <div class="abs footer__social" aria-label="Social links"><span></span><span></span><span></span><span></span></div>
  <p class="abs footer__copy">Copyright © 2014 All Right Reserved<br><small>LINDAVO.INC</small></p>
  <div class="abs footer__rule"></div>
  <div class="abs footer__col footer__col--links">
    <h4>QUICK LINKS</h4>
    <ul><li>For Rent</li><li>For Sale</li><li>Apply Online</li><li>Contact</li><li>Site Map</li></ul>
  </div>
  <div class="abs footer__col footer__col--places">
    <h4>LOCTIONS</h4>
    <ul><li>The Harbor</li><li>The Maple</li><li>Ridgeview Apartment</li><li>Shoreline</li></ul>
  </div>
  <div class="abs footer__col footer__col--member">
    <h4>MEMBERSHIP</h4>
    <p>Civic Renewal Alliance Eastern Planning Guild Regional Planning Officers State Neighborhood Growth Society</p>
  </div>

</div>
</body>
</html>
```